Book Cover Quieting Gnats, Shouldn'ts and Maybes, Climbing out of the valley of sorrow

Need a book cover design for my new web site..Drpeterwalsby.com (website under construction) I'm appearing on Echo of Meridia radio show and want to add a cover design of my book.

My book with enpower people to break the chain of limiting beliefs and unlock their true potential so they will finally experience the life of their dreams

Radio

```html
<!DOCTYPE html>
<html lang="en">
<head>
<meta charset="utf-8">
<title>Quieting Gnats, Shouldn'ts and Maybes — Book Cover</title>
<link rel="stylesheet" href="https://fonts.googleapis.com/css2?family=PT+Sans:ital,wght@1,400&family=Roboto+Condensed:ital,wght@1,700&display=swap">
<style>
  :root {
    --ink-deep: #0d0d0d;
    --stone-dark: #3a3a3a;
    --stone-mid: #8c8a86;
    --stone-light: #d9d6d0;
    --glow: #fbf8ee;
    --sky: #8fc4ee;
    --sky-deep: #4a9ae0;
    --type-cream: #f2eee2;
    --type-shadow: rgba(0, 0, 0, 0.85);
  }
  html, body {
    margin: 0;
    padding: 0;
    width: 800px;
    height: 1200px;
    overflow: hidden;
    background: var(--ink-deep);
  }
  .cover {
    position: relative;
    width: 800px;
    height: 1200px;
    overflow: hidden;
    background: var(--ink-deep);
  }
  .cover-art {
    position: absolute;
    inset: 0;
    background:
      radial-gradient(ellipse 120px 140px at 430px 450px, var(--sky) 0%, var(--sky-deep) 55%, rgba(74,154,224,0) 100%),
      radial-gradient(ellipse 260px 280px at 420px 460px, var(--glow) 0%, rgba(251,248,238,0.6) 40%, rgba(251,248,238,0) 100%),
      radial-gradient(ellipse 460px 560px at 420px 470px, var(--stone-light) 0%, var(--stone-mid) 45%, var(--stone-dark) 75%, var(--ink-deep) 100%),
      linear-gradient(to bottom, var(--stone-dark) 0%, var(--ink-deep) 100%);
  }
  .subtitle {
    position: absolute;
    top: 38px;
    left: 0;
    width: 800px;
    margin: 0;
    text-align: center;
    font-family: "PT Sans", sans-serif;
    font-style: italic;
    font-weight: 400;
    font-size: 33px;
    color: var(--type-cream);
    text-shadow: 0 2px 6px var(--type-shadow);
  }
  .title {
    position: absolute;
    top: 828px;
    left: 0;
    width: 800px;
    margin: 0;
    font-family: "Roboto Condensed", sans-serif;
    font-style: italic;
    font-weight: 700;
    color: var(--type-cream);
    text-shadow: 3px 5px 8px var(--type-shadow);
    line-height: 1;
  }
  .title-lead {
    display: block;
    margin-left: 205px;
    font-size: 90px;
    letter-spacing: -1px;
  }
  .title-link {
    display: block;
    margin-left: 283px;
    margin-top: -4px;
    font-size: 30px;
  }
  .title-main {
    display: block;
    text-align: center;
    margin-top: 6px;
    font-size: 86px;
    letter-spacing: -1px;
  }
  .title-main .small {
    font-size: 32px;
    letter-spacing: 0;
  }
  .author {
    position: absolute;
    top: 1083px;
    right: 52px;
    margin: 0;
    font-family: "Roboto Condensed", sans-serif;
    font-style: italic;
    font-weight: 700;
    font-size: 30px;
    color: var(--type-cream);
    text-shadow: 0 2px 6px var(--type-shadow);
  }
</style>
</head>
<body>
  <main class="cover">
    <div class="cover-art" role="img" aria-label="Illustration of a cracked stone wall bursting open, light rays streaming through a hole that reveals blue sky and clouds"></div>
    <p class="subtitle">Quieting Gnats, Shouldn'ts and Maybes</p>
    <h1 class="title">
      <span class="title-lead">Climbing</span>
      <span class="title-link">out of the</span>
      <span class="title-main">Valley <span class="small">of</span> Sorrow</span>
    </h1>
    <p class="author">Dr Peter Walsby M.D.</p>
  </main>
</body>
</html>
```